Dune Air & Plus business card

I need an awesome, double-sided business card designed with our new logo. I would like the one side black with the colored logo, and the back side is all yours. I'd like to see horizontal and vertical layouts. Get creative! Thank you.

Target Market(s)

HVAC, Heating and Cooling in Phoenix, AZ

Industry/Entity Type

HVAC

Contact Information for Business Card

We need our new logo on the card. Tom Harker, (623) 555-0142, tom@trydunesair.com, www.trydunesair.com, ROC 514273

```html
<!DOCTYPE html>
<html lang="en">
<head>
<meta charset="utf-8">
<title>Dune Air &amp; Plus business card</title>
<link href="https://fonts.googleapis.com/css2?family=Exo+2:wght@400;500;700;800&display=swap" rel="stylesheet">
<style>
  :root {
    --backdrop: #4d4d4d;
    --card-white: #ffffff;
    --card-black: #141414;
    --brand-blue: #0a58b8;
    --brand-blue-light: #0b74d4;
    --brand-blue-dark: #033f94;
    --brand-orange: #f0641e;
    --text-light: #ffffff;
  }
  * { box-sizing: border-box; margin: 0; padding: 0; }
  html, body {
    width: 1075px; height: 1200px; overflow: hidden;
    background: var(--backdrop);
    font-family: "Exo 2", sans-serif;
  }
  .card {
    position: absolute; left: 206px; width: 663px; height: 395px;
    overflow: hidden;
    box-shadow: 3px 3px 2px rgba(0,0,0,0.45);
  }
  .card--front { top: 187px; background: var(--card-white); }
  .card--back { top: 637px; background: var(--card-black); }

  .brand-name {
    position: absolute;
    display: flex; align-items: center; gap: 12px;
    font-family: "Exo 2", sans-serif; font-weight: 800;
    color: var(--brand-blue); white-space: nowrap;
  }
  .brand-name__dot {
    width: 18px; height: 18px; border-radius: 50%;
    background: var(--brand-orange); flex: none;
  }
  .card--front .brand-name { right: 44px; top: 110px; font-size: 36px; }
  .card--back .brand-name {
    left: 0; right: 0; top: 170px; justify-content: center; font-size: 44px;
    color: var(--brand-blue-light);
  }

  .holder-name {
    position: absolute; left: 37px; top: 240px;
    font-weight: 800; font-size: 24px; letter-spacing: 1px;
    color: var(--brand-blue-dark);
  }
  .holder-rule {
    position: absolute; left: 37px; top: 276px; width: 190px; height: 4px;
    background: var(--brand-orange);
  }
  .contact-band {
    position: absolute; left: 0; top: 279px; width: 100%; height: 116px;
    background: linear-gradient(180deg, var(--brand-blue-light), var(--brand-blue-dark));
  }
  .contact-list {
    position: absolute; left: 35px; top: 17px; list-style: none;
    color: var(--text-light); font-size: 17px; font-weight: 500;
  }
  .contact-list li { display: flex; align-items: center; gap: 6px; height: 24px; }
  .contact-list svg { width: 17px; height: 17px; flex: none; }
  .license {
    position: absolute; right: 41px; top: 73px;
    color: var(--text-light); font-size: 17px; font-weight: 500;
  }
</style>
</head>
<body>
  <section class="card card--front">
    <div class="brand-name"><span class="brand-name__dot"></span>Dune Air &amp; Plus</div>
    <h1 class="holder-name">TOM HARKER</h1>
    <div class="holder-rule"></div>
    <div class="contact-band">
      <ul class="contact-list">
        <li>
          <svg viewBox="0 0 24 24" fill="none" stroke="#f0641e" stroke-width="2.2"><path d="M5 3h4l2 5-2.5 1.5a11 11 0 0 0 6 6L16 13l5 2v4a2 2 0 0 1-2 2A16 16 0 0 1 3 5a2 2 0 0 1 2-2z"/></svg>
          (623) 555-0142
        </li>
        <li>
          <svg viewBox="0 0 24 24" fill="#f0641e"><path d="M2 5h20v14H2z"/><path d="M2 5l10 8 10-8" fill="none" stroke="#0a58b8" stroke-width="1.6"/></svg>
          tom@trydunesair.com
        </li>
        <li>
          <svg viewBox="0 0 24 24" fill="none" stroke="#f0641e" stroke-width="2"><circle cx="12" cy="12" r="9"/><path d="M3 12h18M12 3c3 3 3 15 0 18M12 3c-3 3-3 15 0 18"/></svg>
          www.trydunesair.com
        </li>
      </ul>
      <div class="license">ROC 514273</div>
    </div>
  </section>

  <section class="card card--back">
    <div class="brand-name"><span class="brand-name__dot"></span>Dune Air &amp; Plus</div>
  </section>
</body>
</html>
```